"VaduMakers" Graphic Design Project

We are a new business creating bath/ body/beauty products. We need label designs for men "Lusto for Men " and women- "Lusto for Women" . Since the collection called Lusto will be used for both- we'd like the labels to look similar but separating the gender look- maybe by a same color variation. Our bottles are amber in color , so we like the beiges, cream, and earthy warm tones - greens- brown-orange- yellow-colors. The labels are for 8 oz amber cosmo round bottles. The height is 7.32inches and the diameter is 1.85 inches.
Our starting line will be Lusto for Men ( Silk Body Wash, Silk Body Lotion and Body Mist) and the same for Lusto for Women.
Updates

Target Market(s)

Our target audience is between 30 to 60 years of age. Salons and private consumers.
I am including attached sample of what was started by me.

Industry/Entity Type

Business

Requirements
Must have
• We would like to incorporate the company name- VaduMakers along with the name of the product- which will be Lusto for Men or Lusto for Women on each label.

On label with company name or somewhere on label we would like a tree to symbolize the beginning, but we are open to suggestions.

```html
<!DOCTYPE html>
<html lang="en">
<head>
<meta charset="utf-8">
<title>Lusto Silk Body Wash Labels – VaduMakers</title>
<link rel="stylesheet" href="https://fonts.googleapis.com/css2?family=Josefin+Sans:wght@300;400;600;700&display=swap">
<style>
  :root {
    --men-frame: #123f1f;
    --men-edge: #c9dc98;
    --men-center: #f1f6dc;
    --men-title: #1d4a25;
    --men-text: #1b2a12;
    --men-brand: #2b9ea0;
    --men-tree-top: #3aa8a8;
    --men-tree-trunk: #6a3a22;

    --women-frame: #5a1a0b;
    --women-edge: #c4b86c;
    --women-center: #f2eecb;
    --women-title: #8c4a1c;
    --women-text: #7a2c0e;
    --women-brand: #d9822b;
    --women-tree-top: #d99a2e;
    --women-tree-trunk: #6a3016;

    --gap: #ffffff;
  }

  * { box-sizing: border-box; margin: 0; padding: 0; }

  html, body {
    width: 1200px;
    height: 570px;
    overflow: hidden;
    background: var(--gap);
  }

  .sheet {
    position: relative;
    width: 1200px;
    height: 570px;
    font-family: "Josefin Sans", Arial, sans-serif;
  }

  .label {
    position: absolute;
    top: 0;
    width: 598px;
    height: 570px;
    background: radial-gradient(ellipse at 50% 42%, var(--center) 0%, var(--edge) 85%);
    color: var(--text);
  }

  .label--men {
    left: 0;
    --frame: var(--men-frame);
    --edge: var(--men-edge);
    --center: var(--men-center);
    --title: var(--men-title);
    --text: var(--men-text);
    --brand: var(--men-brand);
    --tree-top: var(--men-tree-top);
    --tree-trunk: var(--men-tree-trunk);
    --axis: 304px;
  }

  .label--women {
    left: 602px;
    --frame: var(--women-frame);
    --edge: var(--women-edge);
    --center: var(--women-center);
    --title: var(--women-title);
    --text: var(--women-text);
    --brand: var(--women-brand);
    --tree-top: var(--women-tree-top);
    --tree-trunk: var(--women-tree-trunk);
    --axis: 294px;
  }

  .label__frame {
    position: absolute;
    inset: 5px;
    border: 6px solid var(--frame);
    pointer-events: none;
  }

  .label__title,
  .label__audience,
  .label__product,
  .label__brand,
  .label__volume {
    position: absolute;
    left: calc(var(--axis) - 150px);
    width: 300px;
    text-align: center;
    white-space: nowrap;
  }

  .label__title {
    top: 16px;
    font-weight: 300;
    font-size: 62px;
    line-height: 1;
    color: var(--title);
  }

  .label__audience {
    top: 95px;
    font-weight: 300;
    font-size: 22px;
    line-height: 1;
    color: var(--title);
  }

  .label__product {
    top: 134px;
    font-weight: 300;
    font-size: 15px;
    line-height: 1;
    color: var(--text);
  }

  .label__brand {
    top: 192px;
    font-weight: 600;
    font-size: 35px;
    line-height: 1;
    color: var(--brand);
  }

  .label__tree {
    position: absolute;
    top: 264px;
    width: 168px;
    height: 248px;
    left: calc(var(--axis) - 84px);
    border-radius: 50% 50% 8px 8px / 40% 40% 8px 8px;
    background: linear-gradient(180deg, var(--tree-top) 0%, var(--tree-top) 58%, var(--tree-trunk) 100%);
    opacity: 0.85;
  }
  .label--women .label__tree { width: 156px; left: calc(var(--axis) - 78px); }

  .label__volume {
    top: 522px;
    font-weight: 300;
    font-size: 15px;
    line-height: 1;
    color: var(--text);
  }

  .label__info {
    position: absolute;
    text-align: center;
    white-space: nowrap;
    font-weight: 300;
    font-size: 13px;
    line-height: 18.4px;
  }
  .label--men .label__info { top: 73px; left: 14px; width: 200px; }
  .label--women .label__info { top: 71px; left: 4px; width: 180px; }

  .label__info p + p { margin-top: 16px; }

  .label__ingredients {
    position: absolute;
    text-align: center;
    white-space: nowrap;
    font-weight: 600;
    font-size: 10.6px;
  }
  .label--men .label__ingredients { top: 77px; left: 428px; width: 120px; line-height: 14.3px; }
  .label--women .label__ingredients { top: 73px; left: 436px; width: 120px; line-height: 13.8px; }

  .label__ingredients-heading { font-weight: 400; }
</style>
</head>
<body>
<main class="sheet">

  <section class="label label--men" aria-label="Lusto for Men Silk Body Wash label">
    <div class="label__frame"></div>

    <div class="label__info">
      <p>Our Nourishing<br>Silk Body Wash<br>will engulf you<br>in luxurious lather<br>as it gently cleanses<br>your delicate skin<br>leaving it soft as silk.</p>
      <p>Directions:<br>Apply to skin while damp<br>with sponge or wash cloth.<br>Rinse well.</p>
      <p>WARNINGS/CAUTIONS:<br>For external use only.<br>Avoid contact with eyes.</p>
      <p>NOT TESTED ON ANIMALS<br>MADE IN USA<br>VaduMakers<br>Bath - Body - Home<br>Palmview, FL 33190<br>Shop 24/7<br>www.vadumakers.com</p>
    </div>

    <h1 class="label__title">Lusto</h1>
    <p class="label__audience">for men</p>
    <p class="label__product">Silk Body Wash</p>
    <p class="label__brand">VaduMakers</p>
    <div class="label__tree" role="img" aria-label="Illustration of a tree with teal leaves and a brown trunk"></div>
    <p class="label__volume">8.25 fl oz. / 244 ml.</p>

    <div class="label__ingredients">
      <span class="label__ingredients-heading">INGREDIENTS:</span><br>
      purified water, sodium<br>olefin sulfonate (plant<br>source), organic aloe<br>barbadensis leaf<br>juice, cocamidopro-<br>pyl betaine (plant<br>source), sodium<br>chloride (salt), kosher<br>vegetable glycerin,<br>tocopherol (natural<br>vitamin E), polyso-<br>rbate 20 (plant source),<br>potassium sorbate<br>(plant source),<br>phenoxyethanol<br>(mild preservative),<br>caprylyl glycol<br>(plant source),<br>organic anthemis<br>nobilis (chamomile)<br>extract, organic<br>calendula officinalis<br>flower extract, xanthan<br>gum (plant source),<br>magnesium ascorbyl<br>phosphate (vitamin C<br>ester), sodium bi-<br>carbonate (baking<br>soda), citric acid<br>fragrance.
    </div>
  </section>

  <section class="label label--women" aria-label="Lusto for Women Silk Body Wash label">
    <div class="label__frame"></div>

    <div class="label__info">
      <p>Our Nourishing<br>Silk Body Wash<br>will engulf you<br>in luxurious lather<br>as it gently cleanses<br>your delicate skin<br>leaving it soft as silk.</p>
      <p>Directions:<br>Apply to skin while damp<br>with sponge or wash cloth.<br>Rinse well.</p>
      <p>WARNINGS/CAUTIONS:<br>For external use only.<br>Avoid contact with eyes.</p>
      <p>NOT TESTED ON ANIMALS<br>MADE IN USA<br>VaduMakers<br>Bath - Body - Home<br>Palmview, FL 33190<br>Shop 24/7<br>www.vadumakers.com</p>
    </div>

    <h1 class="label__title">Lusto</h1>
    <p class="label__audience">for women</p>
    <p class="label__product">Silk Body Wash</p>
    <p class="label__brand">VaduMakers</p>
    <div class="label__tree" role="img" aria-label="Illustration of a tree with golden autumn leaves and a brown trunk"></div>
    <p class="label__volume">8.25 fl oz. / 244 ml.</p>

    <div class="label__ingredients">
      <span class="label__ingredients-heading">INGREDIENTS:</span><br>
      purified water, sodium<br>olefin sulfonate (plant<br>source), organic aloe<br>barbadensis leaf<br>juice, cocamidopro-<br>pyl betaine (plant<br>source), sodium<br>chloride (salt), kosher<br>vegetable glycerin,<br>tocopherol (natural<br>vitamin E), polyso-<br>rbate 20 (plant source),<br>potassium sorbate<br>(plant source),<br>phenoxyethanol<br>(mild preservative),<br>caprylyl glycol<br>(plant source),<br>organic anthemis<br>nobilis (chamomile)<br>extract, organic<br>calendula officinalis<br>flower extract, xanthan<br>gum (plant source),<br>magnesium ascorbyl<br>phosphate (vitamin C<br>ester), sodium bi-<br>carbonate (baking<br>soda), citric acid<br>fragrance.
    </div>
  </section>

</main>
</body>
</html>
```